Creat new BusinessCard for Brightpath Advisory!

Hello Creativ Designer. I need a new Businesscard for our brand new Company "Brightpath Coaching". We do Consulting for a better Life & Work Situation. to create Fulfillment, Sense, Motivation and healthy Work Places in Company's. So we try to create a better World and help the employee to like what they do!
So we would like to have 2 Sites on the card. On the Back we want to put this words: "A meaningful life is one spent serving others" (it can be vertical oder horizontal). In the front there is the Logo (Black or White) and Adress+ and Slogan.

Slogan on the front: -Shape your Work & Life into something better-

Name: Lukas Fenwald
Titel: Founder - Visionary - Trainer
Adress: Based in Switzerland

Tel: +41 (0) 71 483 27 15
Email: hello@brightpath-coaching.ch
Homepage: www.brightpath-coaching.ch

Thanks for your inspired Ideas and your help to make the world to a better place! IT has to be ready to print and normal Size.

Target Market(s)

insurance, Bank, Telecom, industry, IT, Medical

Contact Information for Business Card

Breite: 85 mm x Höhe: 55 mm

Colors

Designer to choose colors to be used in the design.

Requirements
Nice to have
• Thanks for your Ideas so far!
• Maybe you can try/play with the colors: Purple Code #652C8F and Grey #979797 from the Zorvik Logo purple and grey (but only a soft combination, not to much)

```html
<!DOCTYPE html>
<html lang="en">
<head>
<meta charset="utf-8">
<title>Brightpath Coaching – Business Card</title>
<link href="https://fonts.googleapis.com/css2?family=Open+Sans:wght@400;600;700&family=Oswald:wght@400;500&display=swap" rel="stylesheet">
<style>
  :root {
    --stage: #e9e6e1;
    --ink: #1f1f1f;
    --panel-dark: #232323;
    --paper: #ffffff;
    --gold: #b59a5a;
    --gold-soft: #c6ad6e;
    --muted: #d8d8d8;
    --rule: #8a8a8a;
  }
  * { box-sizing: border-box; margin: 0; padding: 0; }
  html, body { width: 1200px; height: 840px; overflow: hidden; }
  body {
    background: var(--stage);
    font-family: "Open Sans", Arial, sans-serif;
    display: flex;
    align-items: center;
    justify-content: center;
    gap: 56px;
  }
  .card {
    width: 520px;
    height: 336px;
    position: relative;
    overflow: hidden;
    box-shadow: 0 14px 30px rgba(0,0,0,0.18);
  }

  /* wordmark */
  .brand-name {
    font-family: "Open Sans", Arial, sans-serif;
    font-weight: 700;
    color: var(--ink);
    text-transform: uppercase;
    letter-spacing: 0.6px;
    line-height: 1.1;
  }

  /* front side */
  .card-front { display: flex; background: var(--paper); }
  .front-brand {
    width: 52%;
    background: var(--paper);
    padding: 0 30px;
    display: flex;
    flex-direction: column;
    justify-content: center;
    align-items: center;
    text-align: center;
  }
  .front-brand .brand-name { font-size: 22px; }
  .brand-rule {
    width: 190px; height: 1px; background: var(--rule); margin: 12px 0 14px;
  }
  .slogan {
    font-size: 13px;
    color: var(--ink);
    line-height: 1.5;
  }
  .front-contact {
    width: 48%;
    background: var(--panel-dark);
    color: var(--paper);
    padding: 54px 24px 0 26px;
  }
  .person-name {
    font-family: "Oswald", "Arial Narrow", sans-serif;
    font-weight: 400;
    font-size: 24px;
    letter-spacing: 0.5px;
    text-transform: uppercase;
    line-height: 1;
  }
  .person-name .surname { color: var(--gold-soft); font-weight: 500; }
  .person-title { font-size: 11.5px; color: var(--muted); margin-top: 6px; }
  .contact-rule { height: 1px; background: var(--rule); margin: 16px 0 18px; }
  .contact-list { list-style: none; }
  .contact-list li {
    display: flex; align-items: center; gap: 10px;
    font-size: 12px; margin-bottom: 9px; color: var(--paper);
    white-space: nowrap;
  }
  .contact-list svg { width: 15px; height: 15px; flex: none; }

  /* back side */
  .card-back { background: var(--ink); display: flex; flex-direction: column; }
  .back-top { height: 24px; background: var(--ink); }
  .back-main {
    height: 246px;
    background: var(--paper);
    display: flex;
    align-items: center;
    justify-content: center;
  }
  .back-main .brand-name { font-size: 28px; }
  .back-quote {
    height: 40px;
    background: var(--gold);
    display: flex; align-items: center; justify-content: center;
    font-size: 16px;
    color: var(--ink);
    letter-spacing: 0.2px;
  }
  .back-bottom { flex: 1; background: var(--ink); }
</style>
</head>
<body>

  <section class="card card-front" aria-label="Business card front">
    <div class="front-brand">
      <span class="brand-name">Brightpath<br>Coaching</span>
      <div class="brand-rule"></div>
      <p class="slogan">Shape your Work &amp; Life<br>into something better</p>
    </div>
    <div class="front-contact">
      <h1 class="person-name">Lukas <span class="surname">Fenwald</span></h1>
      <p class="person-title">Founder-Visionary-Trainer</p>
      <div class="contact-rule"></div>
      <ul class="contact-list">
        <li>
          <svg viewBox="0 0 16 16" aria-hidden="true"><path fill="#b59a5a" d="M3.6 1.5l2.3 2.6-1.2 1.6c.9 2 2.6 3.7 4.6 4.6l1.6-1.2 2.6 2.3-1.2 2.4C7 13.5 2.5 9 1.2 2.7z"/></svg>
          +41 (0) 71 483 27 15
        </li>
        <li>
          <svg viewBox="0 0 16 16" aria-hidden="true"><rect x="1" y="3" width="14" height="10" fill="#b59a5a"/><path d="M1 3.5l7 5 7-5" fill="none" stroke="#232323" stroke-width="1.2"/></svg>
          hello@brightpath-coaching.ch
        </li>
        <li>
          <svg viewBox="0 0 16 16" aria-hidden="true"><circle cx="8" cy="8" r="6.5" fill="none" stroke="#b59a5a" stroke-width="1.4"/><ellipse cx="8" cy="8" rx="2.8" ry="6.5" fill="none" stroke="#b59a5a" stroke-width="1.1"/><path d="M1.5 8h13" stroke="#b59a5a" stroke-width="1.1"/></svg>
          www.brightpath-coaching.ch
        </li>
      </ul>
    </div>
  </section>

  <section class="card card-back" aria-label="Business card back">
    <div class="back-top"></div>
    <div class="back-main">
      <span class="brand-name">Brightpath Coaching</span>
    </div>
    <p class="back-quote">A meaningful life is one spent serving others</p>
    <div class="back-bottom"></div>
  </section>

</body>
</html>
```